Tolvek Acres brand , chocolate packaging design

Tolvek Acres

Products List

CANNABIS INFUSED CHOCOLATE BAR
(4 Flavor Chocolate Bar)
Original Milk chocolate Bar
Cookies N Cream Bar
Strawberry Cheesecake Bar
S’mores Bar

Information Front
-1000 MG THC Per package
-100mg THC per serving
-Made with Belgian Chocolate
-Made with Quality California Cannabis Extracts
-Net weight of bar 50grams
-California triangle warning symbol
-Flavor of chocolate bar

Information Back

-10 Servings per package
-100 mg serving size

-Directions
Wait 1-2 hours for full effect before consuming more.
-Very potent , Keep out of reach of children

-Store at 68-77° F
-Will melt in prolonged heat
-California government warning and p65warning website

Ingredient list

Milk chocolate Bar
MILK CHOCOLATE (SUGAR, COCOA BUTTER , UNSWEETENED CHOCOLATE, SUNFLOWER LECITHIN, VANILLA) , CANNABIS EXTRACT.
ALLERGENS-CONTAINS MILK

Strawberry Cheesecake
WHITE CHOCOLATE (SUGAR, COCOA BUTTER, WHOLE MILK POWDER ,SOY LECITHIN, NATURAL VANILLA FLAVOR) STRAWBERRY POWDER , STRAWBERRY EXTRACT , NATURAL FLAVORS, CANNABIS EXTRACT.

Cookies n cream
WHITE CHOCOLATE (SUGAR, COCOA BUTTER, WHOLE MILK POWDER ,SOY LECITHIN, NATURAL VANILLA FLAVOR) 9
BRANZIES (SUGAR, WHITE RICE FLOUR, TAPIOCA STARCH, PALM OIL, CANOLA OIL, WHOLE OAT FLOUR, CORN STARCH , COCOA (PROCESSED WITH ALKALI), INVERT SUGAR, SOY LECITHIN, BAKING SODA, SALT, XANTHAM GUM , CHOCOLATE, ARTIFICIAL FLAVOR, CANNABIS EXTRACT

S’mores
MILK CHOCOLATE (SUGAR, COCOA BUTTER, MILK, UNSWEETENED CHOCOLATE ,SUNFLOWER LECITHIN, VANILLA), MARSHMALLOW (SUGAR ,CORN SYRUP , MODIFIED STARCH, GELATIN, SODIUM HEXAMETAPHOSPHATE, ARTIFICIAL FLAVOR , NATURAL FLAVOR , ARTIFICIAL COLO (BLUE 1)), GRAHAM CRACKER (CORN STARCH, BROWN SUGAR , CORN FLOUR, PALM FAT , SOY FLOUR , SOY BRAN, HONEY, MODIFIED TAPIOCA STARCH, AMMONIUM BICARBONATE, BAKING SODA, SALT, CARAMELIZED SUGAR) NATURAL FLAVOR, CANNABIS EXTRACT.

Looking for simple clean modern design , chocolate bar can be like miravelle of like the Quendrith one with images on it , and gummy is a mylar bag I really like the Quendrith style , I can provide dieline etc thank you !

Target Market(s)

Young adults

Industry/Entity Type

Cannabis , Delta 8 , CBD

Requirements
Must have
• Chocolate bar is box , dielines Included with images
Nice to have
• Simple clean , elegant and modern design , like the miravelle and Quendrith brands , white logo preferred

```html
<!DOCTYPE html>
<html lang="en">
<head>
<meta charset="utf-8">
<title>Tolvek Acres — Cannabis Infused Chocolate Bars</title>
<link rel="stylesheet" href="https://fonts.googleapis.com/css2?family=Bebas+Neue&family=Montserrat:wght@600;700&display=swap">
<style>
  :root {
    --bg: #e4e4e4;
    --white: #ffffff;
    --purple: #574394; --purple-band: #4a3686; --purple-dot: #4c3a88; --purple-ink: #9d90d2;
    --red: #e41f26; --red-band: #c8171f; --red-dot: #c9161d; --red-ink: #f3868a;
    --pink: #c8449a; --pink-band: #b0327f; --pink-dot: #b2358b; --pink-ink: #eba4d3;
    --black: #231f20; --black-band: #3a3536; --black-dot: #3d3839; --black-ink: #6f696a;
  }
  * { margin: 0; padding: 0; box-sizing: border-box; }
  html, body { width: 1200px; height: 721px; overflow: hidden; }
  body { background: var(--bg); position: relative; font-family: "Montserrat", sans-serif; }

  .bar-box {
    position: absolute; top: 52px; width: 235px; height: 538px; overflow: hidden;
    background: var(--face); color: var(--white);
  }
  .bar-box--milk { left: 95px; --face: var(--purple); --band: var(--purple-band); --dot: var(--purple-dot); --dot-ink: var(--purple-ink); }
  .bar-box--cookies { left: 353px; --face: var(--red); --band: var(--red-band); --dot: var(--red-dot); --dot-ink: var(--red-ink); }
  .bar-box--strawberry { left: 611px; --face: var(--pink); --band: var(--pink-band); --dot: var(--pink-dot); --dot-ink: var(--pink-ink); }
  .bar-box--smores { left: 872px; --face: var(--black); --band: var(--black-band); --dot: var(--black-dot); --dot-ink: var(--black-ink); }

  .brand-name {
    position: absolute; top: 18px; left: 0; width: 100%; text-align: center;
    font-family: "Bebas Neue", sans-serif; font-size: 42px; line-height: 1; letter-spacing: 1px;
  }
  .product-band {
    position: absolute; top: 77px; left: 0; width: 100%; height: 59px; background: var(--band);
    display: flex; align-items: center; justify-content: center; text-align: center;
    font-size: 10.5px; font-weight: 700; letter-spacing: 2.4px; line-height: 1.25;
  }
  .flavor-name {
    position: absolute; top: 165px; left: 95px; width: 140px; text-align: center;
    font-family: "Bebas Neue", sans-serif; font-size: 30px; line-height: 36px; letter-spacing: 0.5px;
  }
  .flavor-name--wide { left: 98px; width: 135px; }

  .product-art { position: absolute; left: 0; bottom: 0; width: 235px; height: 170px; }

  .claim {
    position: absolute; left: 14px; width: 70px; height: 70px; border-radius: 50%;
    background: var(--dot); color: var(--dot-ink); z-index: 2;
    display: flex; flex-direction: column; align-items: center; justify-content: center;
    text-align: center; font-weight: 700; line-height: 1.05;
  }
  .claim--total { top: 147px; }
  .claim--serving { top: 224px; }
  .claim--belgian { top: 302px; }
  .claim--extracts { top: 378px; }
  .claim__number { font-size: 15px; }
  .claim__unit { font-size: 9.5px; }
  .claim__note { font-size: 6px; font-weight: 600; margin-top: 1px; }
  .claim__text { font-size: 8.5px; line-height: 1; }
  .claim__text--small { font-size: 8px; }

  .net-weight {
    position: absolute; left: 20px; bottom: 14px; z-index: 2; text-align: center;
    font-family: "Bebas Neue", sans-serif; line-height: 0.9;
  }
  .net-weight__value { font-size: 17px; }
  .net-weight__unit { font-size: 13px; display: block; }
  .warning-mark { position: absolute; right: 10px; bottom: 12px; width: 44px; height: 40px; z-index: 2; }
</style>
</head>
<body>

<section class="bar-box bar-box--milk">
  <div class="brand-name">Tolvek Acres</div>
  <div class="product-band">CANNABIS INFUSED<br>CHOCOLATE BAR</div>
  <div class="flavor-name">Original<br>Milk<br>Chocolate</div>
  <svg class="product-art" viewBox="0 0 235 170" role="img" aria-label="Photo of a milk chocolate bar splashing into a glass of milk">
    <defs><linearGradient id="milk-art" x1="0" y1="0" x2="1" y2="0"><stop offset="0" stop-color="#3a1e14"/><stop offset="0.5" stop-color="#efeeee"/><stop offset="1" stop-color="#2f170f"/></linearGradient></defs>
    <path d="M0 40 L40 30 L80 20 L120 60 L150 10 L175 40 L210 30 L235 45 L235 170 L0 170 Z" fill="url(#milk-art)"/>
  </svg>
  <div class="claim claim--total"><span class="claim__number">1000</span><span class="claim__unit">mg THC</span><span class="claim__note">Per package</span></div>
  <div class="claim claim--serving"><span class="claim__number">100</span><span class="claim__unit">mg THC</span><span class="claim__note">per serving</span></div>
  <div class="claim claim--belgian"><span class="claim__text">Made<br>with<br>★ Belgian ★<br>Chocolate</span></div>
  <div class="claim claim--extracts"><span class="claim__text claim__text--small">Made with<br>Quality<br>★California★<br>Cannabis<br>Extracts</span></div>
  <div class="net-weight"><span class="net-weight__value">50</span><span class="net-weight__unit">Grams</span></div>
  <svg class="warning-mark" viewBox="0 0 44 40" aria-hidden="true"><path d="M22 3 L41 36 L3 36 Z" fill="none" stroke="#fff" stroke-width="3.5" stroke-linejoin="round"/></svg>
</section>

<section class="bar-box bar-box--cookies">
  <div class="brand-name">Tolvek Acres</div>
  <div class="product-band">CANNABIS INFUSED<br>CHOCOLATE BAR</div>
  <div class="flavor-name">Cookies<br>N<br>Cream</div>
  <svg class="product-art" viewBox="0 0 235 170" role="img" aria-label="Photo of chocolate sandwich cookies in white cream">
    <defs><linearGradient id="cookies-art" x1="0" y1="0" x2="0" y2="1"><stop offset="0" stop-color="#e8e4e0"/><stop offset="1" stop-color="#3b2118"/></linearGradient></defs>
    <path d="M0 60 L30 55 L60 45 L95 55 L130 40 L165 58 L200 50 L235 65 L235 170 L0 170 Z" fill="url(#cookies-art)"/>
  </svg>
  <div class="claim claim--total"><span class="claim__number">1000</span><span class="claim__unit">mg THC</span><span class="claim__note">Per package</span></div>
  <div class="claim claim--serving"><span class="claim__number">100</span><span class="claim__unit">mg THC</span><span class="claim__note">per serving</span></div>
  <div class="claim claim--belgian"><span class="claim__text">Made<br>with<br>★ Belgian ★<br>Chocolate</span></div>
  <div class="claim claim--extracts"><span class="claim__text claim__text--small">Made with<br>Quality<br>★California★<br>Cannabis<br>Extracts</span></div>
  <div class="net-weight"><span class="net-weight__value">50</span><span class="net-weight__unit">Grams</span></div>
  <svg class="warning-mark" viewBox="0 0 44 40" aria-hidden="true"><path d="M22 3 L41 36 L3 36 Z" fill="none" stroke="#fff" stroke-width="3.5" stroke-linejoin="round"/></svg>
</section>

<section class="bar-box bar-box--strawberry">
  <div class="brand-name">Tolvek Acres</div>
  <div class="product-band">CANNABIS INFUSED<br>CHOCOLATE BAR</div>
  <div class="flavor-name flavor-name--wide">Strawberry<br>Cheesecake</div>
  <svg class="product-art" viewBox="0 0 235 170" role="img" aria-label="Photo of a strawberry cheesecake slice with strawberry sauce">
    <defs><linearGradient id="strawberry-art" x1="0" y1="0" x2="0" y2="1"><stop offset="0" stop-color="#f2cfc6"/><stop offset="0.6" stop-color="#d9a98a"/><stop offset="1" stop-color="#b0102e"/></linearGradient></defs>
    <path d="M120 30 L150 10 L210 80 L235 110 L235 170 L0 170 L0 140 L100 130 Z" fill="url(#strawberry-art)"/>
  </svg>
  <div class="claim claim--total"><span class="claim__number">1000</span><span class="claim__unit">mg THC</span><span class="claim__note">Per package</span></div>
  <div class="claim claim--serving"><span class="claim__number">100</span><span class="claim__unit">mg THC</span><span class="claim__note">per serving</span></div>
  <div class="claim claim--belgian"><span class="claim__text">Made<br>with<br>★ Belgian ★<br>Chocolate</span></div>
  <div class="claim claim--extracts"><span class="claim__text claim__text--small">Made with<br>Quality<br>★California★<br>Cannabis<br>Extracts</span></div>
  <div class="net-weight"><span class="net-weight__value">50</span><span class="net-weight__unit">Grams</span></div>
  <svg class="warning-mark" viewBox="0 0 44 40" aria-hidden="true"><path d="M22 3 L41 36 L3 36 Z" fill="none" stroke="#fff" stroke-width="3.5" stroke-linejoin="round"/></svg>
</section>

<section class="bar-box bar-box--smores">
  <div class="brand-name">Tolvek Acres</div>
  <div class="product-band">CANNABIS INFUSED<br>CHOCOLATE BAR</div>
  <div class="flavor-name">S’mores</div>
  <svg class="product-art" viewBox="0 0 235 170" role="img" aria-label="Photo of a s'more with graham cracker and melted marshmallow">
    <defs><linearGradient id="smores-art" x1="0" y1="0" x2="1" y2="1"><stop offset="0" stop-color="#c98d4e"/><stop offset="0.5" stop-color="#f3eee8"/><stop offset="1" stop-color="#b8773c"/></linearGradient></defs>
    <path d="M0 40 L60 30 L120 20 L190 40 L235 70 L235 170 L0 170 Z" fill="url(#smores-art)"/>
  </svg>
  <div class="claim claim--total"><span class="claim__number">1000</span><span class="claim__unit">mg THC</span><span class="claim__note">Per package</span></div>
  <div class="claim claim--serving"><span class="claim__number">100</span><span class="claim__unit">mg THC</span><span class="claim__note">per serving</span></div>
  <div class="claim claim--belgian"><span class="claim__text">Made<br>with<br>★ Belgian ★<br>Chocolate</span></div>
  <div class="claim claim--extracts"><span class="claim__text claim__text--small">Made with<br>Quality<br>★California★<br>Cannabis<br>Extracts</span></div>
  <div class="net-weight"><span class="net-weight__value">50</span><span class="net-weight__unit">Grams</span></div>
  <svg class="warning-mark" viewBox="0 0 44 40" aria-hidden="true"><path d="M22 3 L41 36 L3 36 Z" fill="none" stroke="#fff" stroke-width="3.5" stroke-linejoin="round"/></svg>
</section>

</body>
</html>
```